Wordpress Theme, Folder, Brochure

Hello,

I have 3 projects that need to be completed and they all need to be the same theme.

Wordpress Theme:
Design homepage and one internal page

Print Folder:
I need a folder designed to match the website

Trifold Brochure:
I need a generic tri-fold brochure build to match the theme

Please find the attached file for more info.

Dale

```html
<!DOCTYPE html>
<html lang="en">
<head>
<meta charset="utf-8">
<title>Harborline PEO – Payroll Administration</title>
<link href="https://fonts.googleapis.com/css2?family=Source+Sans+3:ital,wght@0,400;0,600;0,700;1,400&display=swap" rel="stylesheet">
<style>
:root{
  --blue:#0b72bb;
  --blue-text:#1a78c2;
  --ink:#333;
  --body:#666;
  --topbar:#4a4b4e;
  --rule:#e2e2e2;
  --foot:#f3f3f3;
  --foot-base:#e8e8e8;
}
*{margin:0;padding:0;box-sizing:border-box}
html,body{width:1153px;height:1200px;overflow:hidden;background:#fff}
body{font-family:"Source Sans 3",sans-serif;color:var(--body);position:relative}
a{color:inherit;text-decoration:none}
ul{list-style:none}

.topbar{position:absolute;left:0;top:0;width:1153px;height:28px;background:linear-gradient(#5b5c60,var(--topbar))}
.topbar-links{position:absolute;right:180px;top:0;height:28px;display:flex;align-items:center;font-size:7.6px;font-weight:600;color:#fff}
.topbar-links li{padding:0 16px;border-left:1px solid #ddd;line-height:8px}
.topbar-links li:first-child{border-left:none}
.topbar-links li:last-child{padding-right:0}

.header{position:absolute;left:0;top:28px;width:1153px;height:82px}
.brand{position:absolute;left:173px;top:28px;display:flex;align-items:center;gap:6px;font-size:22px;font-weight:700;color:var(--blue)}
.brand-dot{width:12px;height:12px;border-radius:50%;background:var(--blue)}
.account-links{position:absolute;top:37px;font-size:9.6px;color:#444}
.account-links a{position:absolute;white-space:nowrap}
.contact-box{position:absolute;left:828px;top:21px;width:160px;height:40px}
.contact-box svg{position:absolute;left:0;top:0}
.contact-label{position:absolute;left:52px;top:3px;font-size:9.6px;color:#444}
.contact-phone{position:absolute;left:52px;top:14px;font-size:15.6px;color:var(--blue)}

.mainnav{position:absolute;left:0;top:110px;width:1153px;height:32px;background:var(--blue)}
.mainnav ul{position:absolute;left:175px;top:0;width:805px;height:32px;display:flex;justify-content:space-between;align-items:center;font-size:9.8px;font-weight:700;color:#fff}
.mainnav li{display:flex;align-items:center;gap:6px}
.mainnav li::after{content:"";width:4px;height:4px;border-right:1.3px solid #cfe4f5;border-bottom:1.3px solid #cfe4f5;transform:rotate(45deg) translateY(-2px)}

.sidenav{position:absolute;left:173px;top:155px;width:188px}
.sidenav li{height:33.7px;display:flex;align-items:center;justify-content:space-between;padding:0 16px 0 17px;font-size:9.5px;font-style:italic;color:var(--blue-text);background:linear-gradient(#fff,#f1f1f1);border-bottom:1px solid #fff}
.sidenav li::after{content:"»";font-style:normal;color:#aaa;font-size:9px}
.sidenav li.is-active{background:var(--blue);color:#fff}
.sidenav li.is-active::after{color:#fff}

.content{position:absolute;left:382px;top:155px;width:598px}
.page-title{height:43px;background:linear-gradient(#fff,#f0f0f0);border-bottom:1px solid var(--rule);padding:15px 0 0 19px;font-size:11px;font-weight:600;color:var(--blue-text)}
.article{padding:17px 0 0 15px;font-size:8.7px;line-height:14.8px}
.article p{margin-bottom:14.8px}
.article h2{font-size:11px;font-weight:600;color:var(--blue-text);margin:0 0 5px;line-height:13px}
.article p.lead{font-weight:600;color:var(--ink);margin-bottom:6px}
.options{margin-bottom:15px}
.options li{font-style:italic;color:var(--blue-text);line-height:20.6px;padding-left:14px;position:relative}
.options li::before{content:"→";position:absolute;left:3px;font-style:normal;color:#999;font-size:7px}
.article .tight{margin-bottom:11px}

.clients{position:absolute;left:0;top:890px;width:1153px;height:92px;border-top:1px solid var(--rule)}
.clients h3{position:absolute;left:0;width:1125px;top:16px;text-align:center;font-size:12px;font-weight:400;color:#555}
.client-row{position:absolute;left:181px;top:50px;width:766px;display:flex;justify-content:space-between;font-size:16px;font-weight:600;color:#9a9a9a}

.footer{position:absolute;left:0;top:982px;width:1153px;height:156px;background:var(--foot)}
.foot-col{position:absolute;top:20px;font-size:10.6px;color:#555}
.foot-col h4{font-size:11.5px;font-weight:400;color:var(--blue-text);margin-bottom:5px}
.foot-col li{line-height:19.8px;padding-left:8px;position:relative}
.foot-col li::before{content:"•";position:absolute;left:0;font-size:8px;color:#777}
.foot-col li.no-bullet::before{content:none}

.base{position:absolute;left:0;top:1138px;width:1153px;height:62px;background:var(--foot-base)}
.copyright{position:absolute;left:174px;top:22px;font-size:11px;color:#666}
.social{position:absolute;left:921px;top:21px;display:flex;gap:7px}
.social span{width:18px;height:18px;border-radius:2px}
.social .s1{background:#3b5998}
.social .s2{background:#4fb3e8}
</style>
</head>
<body>

<div class="topbar">
  <ul class="topbar-links">
    <li>HOME</li><li>ABOUT US</li><li>REQUEST A QUOTE</li><li>CONTACT US</li><li>SITEMAP</li>
  </ul>
</div>

<header class="header">
  <div class="brand"><span class="brand-dot"></span>Harborline PEO</div>
  <nav class="account-links">
    <a style="left:398px">CLIENT LOGIN</a>
    <a style="left:504px">EMPLOYEE LOGIN</a>
    <a style="left:625px">REFERRAL REWARDS</a>
    <a style="left:758px">DEMO</a>
  </nav>
  <div class="contact-box">
    <svg width="44" height="40" viewBox="0 0 44 40" aria-hidden="true">
      <rect x="4" y="2" width="36" height="33" rx="6" fill="#3a3a3a"/>
      <rect x="9" y="6" width="26" height="17" rx="2" fill="#cfd6dc"/>
      <g fill="#888"><rect x="10" y="26" width="5" height="3"/><rect x="19" y="26" width="5" height="3"/><rect x="28" y="26" width="5" height="3"/></g>
      <ellipse cx="22" cy="38" rx="18" ry="2" fill="#ddd"/>
    </svg>
    <div class="contact-label">CONTACT US</div>
    <div class="contact-phone">1.800.555.0172</div>
  </div>
</header>

<nav class="mainnav">
  <ul>
    <li>PEO PAYROLL SERVICES</li>
    <li>PEO HR SOLUTIONS</li>
    <li>PEO ONLINE SERVICES</li>
    <li>PEO WORKERS COMPENSATION</li>
    <li>PEO EMPLOYEE BENEFITS</li>
    <li>PEO INDUSTRY RESOURCES</li>
  </ul>
</nav>

<aside>
  <ul class="sidenav">
    <li class="is-active">Payroll Administration</li>
    <li>Tax Payment &amp; Filing</li>
    <li>Online Payroll Entry</li>
    <li>Paycard</li>
    <li>Time and Attendance</li>
    <li>General Ledger Interface</li>
    <li>ASO Services</li>
    <li>HPower</li>
  </ul>
</aside>

<main class="content">
  <h1 class="page-title">PAYROLL ADMINISTRATION</h1>
  <div class="article">
    <p>Is dealing with your current payroll company's mistakes just one big headache? Do you feel like you don't get the kind of personal attention and service that you expect and deserve? It's about time someone was on your side. Welcome to Harborline PEO!</p>
    <p>Harborline PEO's professional staff is dedicated to taking away the pain of doing payroll. We understand how important it is to get your payroll done right the first time—every time. Our specialists provide you with smart, friendly, personal-touch service; we keep your mind off payroll hassles and on your bottom line. Make the switch to Harborline PEO today and discover what our clients already have: We don't just meet our customer's expectations, we exceed them!</p>
    <h2>INPUT OPTIONS</h2>
    <p class="lead">Harborline PEO clients have the flexibility of choosing from among several convenient payroll input methods :</p>
    <ul class="options">
      <li>Harborline PEO WebPay, our online payroll entry solution!</li>
      <li>Fax us your payroll</li>
      <li>Call in your payroll</li>
      <li>Email us your payroll</li>
      <li>Drop off your payroll</li>
    </ul>
    <h2>REPORTS</h2>
    <p class="tight">With Harborline PEO's powerful, versatile accounting software working for you, say farewell to all your own report-writing burdens. Our system provides you with a library of thousands of reports, each adaptable to meet your every need. Because we continue to enhance and improve our system's reporting capabilities largely based upon our clients' needs, Harborline PEO's ability to give quick, responsive, accurate information remains second to none in the industry.</p>
    <h2>DIRECT DEPOSIT</h2>
    <p class="tight">Do you wish to deposit your net paycheck into one account, or do you want your paycheck split into 100 separate accounts? Or maybe you're interested in PayCard, another easy and convenient way to get paid? No matter what your personal choice is, Harborline PEO is here to handle all your direct deposit requests. In addition to being able to process unlimited account splits, we also provide next-business-day direct deposit—a rare service among all payroll companies.</p>
    <h2>JOB COSTING</h2>
    <p class="tight">Look no further than Harborline PEO to find solutions on how to track all your payroll costs.</p>
    <h2>GARNISHMENTS AND DEDUCTIONS</h2>
    <p class="tight">Let Harborline PEO relieve you of the hassles of dealing with child support orders, levies, and other garnishments. We administer employee deductions and make timely payments to the garnishing authorities. Whether your deductions are for garnishments, health care benefits, advances or uniforms-- just to name a few, Harborline PEO has got you covered.</p>
    <h2>PTO TRACKING</h2>
    <p>At Harborline PEO, we feel that your employees are your greatest asset. They work hard for you every day, and so you want to make sure they all get paid accurately for the time off they've earned. Like so many other things in an employer's life: it's easier said than done. When you allow Harborline PEO to track your employees' sick, vacation, and personal time based on your own PTO policy, you'll feel like you just went on vacation yourself: a vacation from yet another administrative headache.</p>
  </div>
</main>

<section class="clients">
  <h3>Our Clients</h3>
  <div class="client-row">
    <span>Fernmarket</span><span>Quillon</span><span>Netvora</span><span>Ledgerly</span><span>Halvex</span><span>Corvia</span><span>Brightsoft</span><span>Artura</span><span>Relaynet</span>
  </div>
</section>

<footer class="footer">
  <div class="foot-col" style="left:187px"><h4>Cras mollipurus</h4><ul><li>Integer lobortis</li><li>Curabitur ac</li><li>Phasellus tellus nisl</li><li>Aenean fringilla</li><li>Aliquam commodo</li></ul></div>
  <div class="foot-col" style="left:350px"><h4>Cras mollipurus</h4><ul><li>Integer lobortis</li><li>Curabitur ac</li><li>Phasellus tellus nisl</li><li>Aenean fringilla</li><li>Aliquam commodo</li></ul></div>
  <div class="foot-col" style="left:513px"><h4>Cras mollipurus</h4><ul><li>Integer lobortis</li><li>Curabitur ac</li><li>Phasellus tellus nisl</li><li>Aenean fringilla</li><li>Aliquam commodo</li></ul></div>
  <div class="foot-col" style="left:676px"><h4>Cras mollipurus</h4><ul><li>Integer lobortis</li><li>Curabitur ac</li><li>Phasellus tellus nisl</li><li>Aenean fringilla</li><li>Aliquam commodo</li></ul></div>
  <div class="foot-col" style="left:835px"><h4>Contact us</h4><ul><li>Phone : 555 210 4478</li><li class="no-bullet" style="padding-left:44px">555 2104479</li><li>E-mail : hello@harborlinepeo.example</li></ul></div>
</footer>

<div class="base">
  <div class="copyright">Copyright &nbsp;© &nbsp;2013 &nbsp; Harborline PEO, LLC. &nbsp;&nbsp;All Rights Reserved.</div>
  <div class="social"><span class="s1"></span><span class="s2"></span></div>
</div>

</body>
</html>
```